design a web site for equipment and software pos company

We would a web site similar to the site we whited labed our rbts system .https://tryvelko.com/
website would be on RbTillSystems.com
we would a contact page
877-555-0148

We do not want an exact copy just something similar .
we are tablet po system

we are at

we are selling hardware and software

rb till systems
41 cedar hollow ln
warren, nj 07059
we are cloud based system

Target Market(s)

any retail merchant

Industry/Entity Type

credit card processing in POS asystems

Coding

Coded - Design and coding required

Number of Pages Required

5+ page

Requirements
Must have
• be able to connect webnarra hosting
Nice to have
• modern looking site
Should not have
• any red

```html
<!DOCTYPE html>
<html lang="en">
<head>
<meta charset="utf-8">
<title>RB Till Systems</title>
<link href="https://fonts.googleapis.com/css2?family=Open+Sans:wght@400;600;700;800&display=swap" rel="stylesheet">
<style>
:root{
  --yellow:#e9b81c;
  --black:#000;
  --ink:#1d1d1d;
  --muted:#7a7a7a;
  --light:#f1f2f4;
  --white:#fff;
  --screen-top:#f6f6f6;
  --screen-bottom:#3b3530;
}
*{box-sizing:border-box;margin:0;padding:0}
html,body{width:1200px;height:4076px;overflow:hidden}
body{font-family:"Open Sans",Arial,sans-serif;color:var(--ink);background:var(--white);position:relative}
.abs{position:absolute}
.brand{color:var(--white);font-weight:600;font-size:30px;letter-spacing:-.5px;white-space:nowrap}
.btn{display:inline-block;background:var(--yellow);color:var(--black);font-weight:700;font-size:15px;border-radius:5px;padding:11px 20px;text-decoration:none}
.y{color:var(--yellow)}

/* header */
.site-header{top:0;left:0;width:1200px;height:128px;background:var(--black)}
.site-header .brand{left:110px;top:44px}
.main-nav{left:374px;top:53px;display:flex;gap:32px}
.main-nav a{color:var(--white);font-weight:700;font-size:15px;text-decoration:none}
.main-nav a.active,.main-nav a.login{color:var(--yellow)}
.site-header .btn{left:984px;top:42px}

/* hero */
.hero{top:128px;left:0;width:1200px;height:627px;background:linear-gradient(100deg,#1c1611 0%,#3a2a1c 40%,#2b2017 70%,#5b4a39 100%)}
.hero h1{left:104px;top:180px;color:var(--white);font-size:52px;line-height:52px;font-weight:800}
.hero .btn{left:110px;top:352px}
.scroll-hint{left:588px;top:537px;width:24px;height:38px;border:2px solid #ddd;border-radius:12px}
.scroll-hint::after{content:"";position:absolute;left:9px;top:7px;width:2px;height:8px;background:#ddd}

/* pos system */
.pos{top:755px;left:0;width:1200px;height:1015px}
.sec-title{width:1200px;text-align:center;font-size:38px;font-weight:700}
.pos .sec-title{top:92px}
.feature h3{font-size:21px;font-weight:600;margin-bottom:6px}
.feature p{font-size:14px;color:var(--muted);line-height:21px}
.feature.center{text-align:center;width:280px}
.feature.left{text-align:right;width:270px}
.feature.right{text-align:left;width:270px}
.photo{border-radius:6px}

/* about */
.about{top:1770px;left:0;width:1200px;height:430px;background:linear-gradient(110deg,#2e3136,#4b4f55 50%,#373a3f)}
.about h2{top:105px;width:1200px;text-align:center;color:var(--white);font-size:38px;font-weight:700}
.about p{top:175px;left:245px;width:710px;text-align:center;color:#eee;font-size:14px;line-height:21px}
.about .btn{left:532px;top:272px}

/* solutions */
.solutions{top:2200px;left:0;width:1200px;height:767px}
.solutions h2{top:92px;width:1200px;text-align:center;font-size:40px;line-height:52px;font-weight:700}
.item{width:250px;text-align:center}
.item .icon{height:72px;display:flex;align-items:flex-end;justify-content:center;margin-bottom:14px}
.item h4{font-size:19px;font-weight:600;margin-bottom:14px}
.item.hl h4{color:var(--yellow)}
.item p{font-size:14px;color:var(--muted);line-height:21px}

/* why */
.why{top:2967px;left:0;width:1200px;height:566px;background:var(--light)}
.why h2{top:72px;width:1200px;text-align:center;font-size:40px;line-height:52px;font-weight:700}
.laptop{left:352px;top:3228px;width:496px;height:333px;border:14px solid #e4e6ea;border-bottom-width:20px;border-radius:14px 14px 0 0;background:linear-gradient(180deg,var(--screen-top) 0 45%,var(--screen-bottom) 45% 100%);z-index:2}
.laptop-base{left:296px;top:3561px;width:608px;height:16px;background:linear-gradient(#e9eaee,#b8bac0);border-radius:0 0 40px 40px;z-index:2}

/* footer */
.site-footer{top:3533px;left:0;width:1200px;height:543px;background:var(--black);color:var(--white)}
.site-footer .brand{top:168px;width:1200px;text-align:center}
.fcol{top:262px}
.fcol h5{font-size:19px;font-weight:700;margin-bottom:22px}
.fcol ul{list-style:none}
.fcol li{font-size:14px;line-height:21.5px;padding-left:26px;position:relative}
.fcol li::before{content:"›";position:absolute;left:0;color:var(--yellow);font-weight:700}
.fcol.contact li::before{content:none}
.fcol.contact svg{position:absolute;left:0;top:4px}
.copyright{top:447px;width:1200px;text-align:center;font-size:14px}
</style>
</head>
<body>

<header class="site-header abs">
  <div class="brand abs">RB Till Systems</div>
  <nav class="main-nav abs">
    <a class="active" href="#">HOME</a><a href="#">PRICING</a><a href="#">PAGE FEATURES</a><a href="#">BLOG</a><a href="#">CONTACT US</a><a class="login" href="#">LOGIN</a>
  </nav>
  <a class="btn abs" href="#">TRY FOR FREE</a>
</header>

<section class="hero abs" role="img" aria-label="Cashier in an apron swiping a card at a touchscreen till in a dimly lit restaurant">
  <h1 class="abs">WE ARE <span class="y">SELLING</span><br>HARDWARE AND<br><span class="y">SOFTWARE</span></h1>
  <a class="btn abs" href="#">LEARN MORE</a>
  <div class="scroll-hint abs"></div>
</section>

<section class="pos abs">
  <h2 class="sec-title abs">POS SYSTEM</h2>
  <div class="feature center abs" style="left:460px;top:190px"><h3>POS</h3><p>Lorem ipsum dolor sit amet, consectetur adipiscing elit, sed do e</p></div>
  <div class="photo abs" style="left:502px;top:272px;width:196px;height:150px;background:radial-gradient(#9a9ea4,#fff 70%)" role="img" aria-label="Touchscreen POS terminal with receipt printer and cash drawer"></div>

  <svg class="abs" style="left:0;top:0" width="1200" height="1015" aria-hidden="true">
    <line x1="600" y1="440" x2="600" y2="522" stroke="#ccc"/>
    <line x1="410" y1="550" x2="465" y2="595" stroke="#ddd"/>
    <line x1="790" y1="550" x2="735" y2="595" stroke="#ddd"/>
    <line x1="395" y1="830" x2="455" y2="790" stroke="#ddd"/>
    <line x1="805" y1="830" x2="745" y2="790" stroke="#ddd"/>
    <circle cx="600" cy="690" r="210" fill="none" stroke="#bbb" stroke-width="2" stroke-dasharray="2 6"/>
    <circle cx="600" cy="690" r="188" fill="none" stroke="#ccc" stroke-dasharray="2 5"/>
    <polygon points="490,530 503,525 497,538" fill="var(--yellow)"/>
    <polygon points="768,612 780,608 776,622" fill="var(--yellow)"/>
    <polygon points="422,762 434,768 424,776" fill="var(--yellow)"/>
    <polygon points="690,852 702,848 694,862" fill="var(--yellow)"/>
    <circle cx="600" cy="690" r="166" fill="var(--yellow)"/>
    <circle cx="600" cy="690" r="130" fill="var(--black)"/>
    <text x="600" y="700" text-anchor="middle" fill="#fff" font-family="Open Sans, sans-serif" font-weight="600" font-size="30">RB Till Systems</text>
  </svg>

  <div class="feature left abs" style="left:14px;top:485px"><h3>VIRTUAL DASHBOARDS</h3><p>Lorem ipsum dolor sit amet, consectetur adipiscing elit, sed do e</p></div>
  <div class="photo abs" style="left:288px;top:485px;width:126px;height:78px;background:linear-gradient(#dfe6ee,#b5bec8)" role="img" aria-label="Laptop showing analytics dashboard"></div>
  <div class="feature right abs" style="left:910px;top:485px"><h3>ECOMMERCE</h3><p>Lorem ipsum dolor sit amet, consectetur adipiscing elit, sed do e</p></div>
  <div class="photo abs" style="left:790px;top:488px;width:118px;height:72px;background:linear-gradient(90deg,#3a3f6a,#5a4f8a,#2e6fbf)" role="img" aria-label="Row of smartphones showing online store screens"></div>
  <div class="feature left abs" style="left:14px;top:802px"><h3>KIOSKS</h3><p>Lorem ipsum dolor sit amet, consectetur adipiscing elit, sed do e</p></div>
  <div class="photo abs" style="left:305px;top:788px;width:56px;height:108px;background:linear-gradient(#2b5e9a,#111)" role="img" aria-label="Self-service kiosk stand"></div>
  <div class="feature right abs" style="left:910px;top:802px"><h3>MOBILE</h3><p>Lorem ipsum dolor sit amet, consectetur adipiscing elit, sed do e</p></div>
  <div class="photo abs" style="left:834px;top:792px;width:48px;height:96px;background:linear-gradient(#4a6fd0,#7a6ac8);border:4px solid #222;border-radius:9px" role="img" aria-label="Smartphone with app icons"></div>
</section>

<section class="about abs" role="img" aria-label="Hands tearing a receipt from a card terminal printer">
  <h2 class="abs">ABOUT DEVELOPING <span class="y">RB TILL SYSTEMS</span></h2>
  <p class="abs">Lorem ipsum dolor sit amet, consectetur adipiscing elit, sed do eiusmod tempor incididunt ut labore et dolore magna aliqua. Ut enim ad minim veniam, quis nostrud exercitation ullamco laboris nisi ut aliquip ex ea commodo consequat.</p>
  <a class="btn abs" href="#">LEARN MORE</a>
</section>

<section class="solutions abs">
  <h2 class="abs"><span class="y">THE PERFECT</span> SOLUTION<br>FOR <span class="y">RESTAURANT &amp; RETAIL</span></h2>

  <div class="item abs" style="left:193px;top:240px">
    <div class="icon"><svg width="44" height="56" viewBox="0 0 44 56"><path d="M12 16V10a10 10 0 0 1 20 0v6" fill="none" stroke="#111" stroke-width="4"/><rect x="2" y="16" width="40" height="38" rx="4" fill="#111"/></svg></div>
    <h4>Nemo enim ipsam</h4><p>Lorem ipsum dolor sit amet, conse ctetur adipiscing elit, sed do eiusmod tempor incididunt ut labore</p>
  </div>
  <div class="item hl abs" style="left:475px;top:240px">
    <div class="icon"><svg width="58" height="56" viewBox="0 0 58 56"><path d="M6 2v18M12 2v18M18 2v18M6 20h12M12 20v34" stroke="var(--yellow)" stroke-width="4" fill="none"/><circle cx="30" cy="28" r="10" fill="none" stroke="var(--yellow)" stroke-width="5"/><path d="M48 2c8 6 8 20 0 24v28" stroke="var(--yellow)" stroke-width="6" fill="none"/></svg></div>
    <h4>Nemo enim ipsam</h4><p>Lorem ipsum dolor sit amet, conse ctetur adipiscing elit, sed do eiusmod tempor incididunt ut labore</p>
  </div>
  <div class="item abs" style="left:757px;top:240px">
    <div class="icon"><svg width="60" height="56" viewBox="0 0 60 56"><path d="M30 2h26l-2 8H32z" fill="#111"/><path d="M34 12h20l-4 42H38z" fill="#111"/><path d="M2 30a16 12 0 0 1 32 0z" fill="#111"/><rect x="2" y="34" width="32" height="5" fill="#111"/><path d="M2 43h32a4 4 0 0 1-4 8H6a4 4 0 0 1-4-8z" fill="#111"/></svg></div>
    <h4>Nemo enim ipsam</h4><p>Lorem ipsum dolor sit amet, conse ctetur adipiscing elit, sed do eiusmod tempor incididunt ut labore</p>
  </div>

  <div class="item abs" style="left:193px;top:472px">
    <div class="icon"><svg width="64" height="56" viewBox="0 0 64 56"><path d="M18 2q-3 4 0 8t0 8M26 2q-3 4 0 8t0 8M34 2q-3 4 0 8t0 8" stroke="#111" stroke-width="3" fill="none"/><path d="M4 22h44v14a18 18 0 0 1-18 18h-8A18 18 0 0 1 4 36z" fill="#111"/><path d="M48 26a8 8 0 0 1 0 16" stroke="#111" stroke-width="4" fill="none"/></svg></div>
    <h4>Nemo enim ipsam</h4><p>Lorem ipsum dolor sit amet, conse ctetur adipiscing elit, sed do eiusmod tempor incididunt ut labore</p>
  </div>
  <div class="item abs" style="left:475px;top:472px">
    <div class="icon"><svg width="44" height="70" viewBox="0 0 44 70"><circle cx="22" cy="18" r="16" fill="#111"/><path d="M8 30h28L22 68z" fill="#111"/></svg></div>
    <h4>Nemo enim ipsam</h4><p>Lorem ipsum dolor sit amet, conse ctetur adipiscing elit, sed do eiusmod tempor incididunt ut labore</p>
  </div>
  <div class="item abs" style="left:757px;top:472px">
    <div class="icon"><svg width="60" height="56" viewBox="0 0 60 56"><path d="M8 2h44l6 18H2z" fill="#111"/><path d="M6 22h48v32H6z" fill="none" stroke="#111" stroke-width="5"/><rect x="16" y="32" width="12" height="22" fill="#111"/><rect x="34" y="32" width="12" height="10" fill="#111"/></svg></div>
    <h4>Nemo enim ipsam</h4><p>Lorem ipsum dolor sit amet, conse ctetur adipiscing elit, sed do eiusmod tempor incididunt ut labore</p>
  </div>
</section>

<section class="why abs">
  <h2 class="abs">WHY SELL ANOTHER COMPANY'S<br>POS SYSTEM, <span class="y">WHEN YOU CAN</span><br><span class="y">SELL YOUR OWN?</span></h2>
</section>

<footer class="site-footer abs">
  <div class="brand abs">RB Till Systems</div>
  <div class="fcol abs" style="left:112px"><h5>Company</h5><ul><li>About</li><li>Customers</li><li>Jobs</li><li>Blog</li><li>Press</li></ul></div>
  <div class="fcol abs" style="left:361px"><h5>Resources</h5><ul><li>Support</li><li>Contact us</li><li>Privacy policy</li><li>Terms &amp; Condition</li><li></li></ul></div>
  <div class="fcol abs" style="left:656px"><h5>Quick links</h5><ul><li>How it works</li><li>Pricing</li><li>Products</li><li>Customers</li><li>Faq</li></ul></div>
  <div class="fcol contact abs" style="left:888px"><h5>Contact us</h5><ul>
    <li><svg width="11" height="14" viewBox="0 0 11 14"><path d="M5.5 0A5.5 5.5 0 0 0 0 5.5C0 9 5.5 14 5.5 14S11 9 11 5.5A5.5 5.5 0 0 0 5.5 0zm0 7.5a2 2 0 1 1 0-4 2 2 0 0 1 0 4z" fill="var(--yellow)"/></svg>41 Cedar Hollow Ln<br>Warren, NJ 07059</li>
    <li style="margin-top:21px"><svg width="12" height="12" viewBox="0 0 12 12"><path d="M2.5 0l2.5 3-1.5 1.5a8 8 0 0 0 4 4L9 7l3 2.5L10.5 12C5 12 0 7 0 1.5z" fill="var(--yellow)"/></svg>877-555-0148</li>
    <li><svg width="13" height="10" viewBox="0 0 13 10"><rect width="13" height="10" rx="1" fill="var(--yellow)"/><path d="M0 1l6.5 5L13 1" stroke="#000" fill="none"/></svg>info@rbtillsystems.com</li>
  </ul></div>
  <div class="copyright abs">© Copyright @2021 RB Till Systems | All Rights Reserved</div>
</footer>

<div class="laptop abs" role="img" aria-label="Laptop showing a till screen with order list, payment buttons and menu tiles"></div>
<div class="laptop-base abs"></div>

</body>
</html>
```